Gablestone Inspections Business Card

I need a business card for my new company. The company is going to provide home inspections. The name of the company is Gablestone Inspections. I am not sure if I want a single sided card or a double. I have a logo already that I want to incorporate into the card design. I was wondering if I should incorporate a catch phrase on my card or not. If I did the phrase would be "The Intelligent Choice for Home Inspections" but i am unsure how or if to use it on a card. The following information needs to be on the card.
Home Inspection
My Name: Tobias R. Fenwick Phone Number: 555-317-6420 Email: tfenwick@gablestoneinspections.com Website: www.gablestoneinspections.com NY HI License # 27300592415

```html
<!DOCTYPE html>
<html lang="en">
<head>
<meta charset="UTF-8">
<title>Gablestone Inspections Business Card</title>
<link href="https://fonts.googleapis.com/css2?family=Lato:wght@400;700;900&display=swap" rel="stylesheet">
<style>
  :root {
    --backdrop: #e9e7e4;
    --card: #1c1c1e;
    --sky: #6ec6f0;
    --white: #ffffff;
    --ink: #1c1c1e;
  }
  * { margin: 0; padding: 0; box-sizing: border-box; }
  html, body {
    width: 1200px;
    height: 977px;
    overflow: hidden;
    background: var(--backdrop);
    font-family: "Lato", sans-serif;
  }
  .canvas {
    position: relative;
    width: 1200px;
    height: 977px;
  }
  .card {
    position: absolute;
    left: 250px;
    width: 700px;
    height: 400px;
    background: var(--card);
    border-radius: 26px;
    overflow: hidden;
    box-shadow: 0 10px 28px rgba(0,0,0,0.25);
  }
  .card-front { top: 64px; }
  .card-back { top: 512px; }

  .brand {
    display: flex;
    align-items: center;
    gap: 14px;
    color: var(--white);
    font-weight: 900;
    letter-spacing: 0.04em;
    text-transform: uppercase;
  }
  .brand-mark {
    background: var(--sky);
    flex: none;
  }

  .card-front .brand {
    position: absolute;
    left: 0; right: 0; top: 0; bottom: 0;
    justify-content: center;
    font-size: 40px;
  }
  .card-front .brand-mark { width: 26px; height: 26px; }

  .card-back .brand {
    position: absolute;
    right: 44px;
    top: 70px;
    font-size: 22px;
  }
  .card-back .brand-mark { width: 16px; height: 16px; }

  .rule {
    position: absolute;
    left: 40px;
    top: 262px;
    width: 610px;
    height: 1.5px;
    background: var(--sky);
  }
  .holder-name {
    position: absolute;
    left: 40px;
    top: 208px;
    color: var(--sky);
    font-weight: 900;
    font-size: 38px;
    letter-spacing: 0.01em;
    text-transform: uppercase;
  }
  .license {
    position: absolute;
    right: 50px;
    top: 196px;
    text-align: right;
    font-size: 17px;
    line-height: 1.3;
  }
  .license-label { color: var(--sky); }
  .license-number { color: var(--white); letter-spacing: 0.02em; }

  .contact {
    position: absolute;
    left: 40px;
    top: 276px;
    list-style: none;
    color: var(--white);
    font-size: 18px;
    line-height: 1.55;
  }
  .contact li { display: flex; align-items: center; gap: 10px; }
  .contact svg { width: 15px; height: 15px; fill: var(--sky); flex: none; }

  .footer-shapes {
    position: absolute;
    left: 0; bottom: 0;
    width: 700px;
    height: 70px;
  }
  .website {
    position: absolute;
    right: 32px;
    bottom: 20px;
    color: var(--ink);
    font-size: 16px;
    letter-spacing: 0.02em;
    white-space: nowrap;
  }
</style>
</head>
<body>
<div class="canvas">

  <section class="card card-front">
    <div class="brand">
      <span class="brand-mark"></span>
      <span class="brand-name">Gablestone Inspections</span>
    </div>
  </section>

  <section class="card card-back">
    <div class="brand">
      <span class="brand-mark"></span>
      <span class="brand-name">Gablestone Inspections</span>
    </div>

    <div class="license">
      <div class="license-label">NY HI LIC #</div>
      <div class="license-number">27300592415</div>
    </div>

    <h1 class="holder-name">Tobias R. Fenwick</h1>
    <div class="rule"></div>

    <ul class="contact">
      <li>
        <svg viewBox="0 0 24 24" aria-hidden="true"><path d="M6.6 10.8a15.1 15.1 0 0 0 6.6 6.6l2.2-2.2c.3-.3.7-.4 1-.2 1.1.4 2.300.6 3.6.6.6 0 1 .4 1 1V20c0 .6-.4 1-1 1A17 17 0 0 1 3 4c0-.6.4-1 1-1h3.5c.6 0 1 .4 1 1 0 1.3.2 2.5.6 3.6.1.3 0 .7-.2 1z"/></svg>
        <span>555-317-6420</span>
      </li>
      <li>
        <svg viewBox="0 0 24 24" aria-hidden="true"><path d="M2 5h20v14H2zm2 2v.4l8 5.3 8-5.3V7zm0 2.8V17h16V9.8l-8 5.3z"/></svg>
        <span>tfenwick@gablestoneinspections.com</span>
      </li>
    </ul>

    <svg class="footer-shapes" viewBox="0 0 700 70" aria-hidden="true">
      <polygon points="0,62 360,62 352,70 0,70" fill="#ffffff"/>
      <polygon points="380,10 700,10 700,70 370,70" fill="#6ec6f0"/>
    </svg>
    <div class="website">www.gablestoneinspections.com</div>
  </section>

</div>
</body>
</html>
```